Brightway Merch Webpage

Brightway Merc need a simple, elegant and professional website

As the company is selling products and clothes for companies we would like to have a large picture carousel on the top.
As one of the logos have black background I would like the webpage to be black.

There should also be thre boxes on main page where we can have information about the product of the month, news and other.

On the menu we need:
- Our products
-our catalogues (here we need to have the possibility to upload several pdf and e-catalogues
-About us
-Contact us
-News

Here are som pages in the same branch
http://www.kavlemerke.no/
http://www.tavbrud.no/
http://www.merkelund.no/

I will attach the logo with both white and black background.
The logos are attached in png but I have eps and jpg as well. Just let me know what you need.

looking forward to your designs:)

Brightway Merch is a company that provides corporate profile products such as logo on t-shirts, work uniform, pens, cups etc. We also work with event companies that need advertising and profile products for theirs event as well as the sports segment.

Target Market(s)

corporate, eventcompanies and sportsegment

Industry/Entity Type

Advertising

Requirements
Must have
• Facebook, twitter and like button for social media

```html
<!DOCTYPE html>
<html lang="en">
<head>
<meta charset="utf-8">
<title>Brightway Merc</title>
<link rel="stylesheet" href="https://fonts.googleapis.com/css2?family=Oswald:wght@400;600&family=Pathway+Gothic+One&family=Lato:wght@400;700&display=swap">
<style>
:root{
  --black:#000;
  --brand-blue:#1a9ad8;
  --light-blue:#7cc6ee;
  --deep-blue:#0a5e9c;
  --orange:#f08a1c;
  --nav-top:#f7f7f7;
  --nav-bottom:#d9d9d9;
  --nav-text:#555;
  --card-grey:#e6e7e9;
  --title-grey:#444;
  --content-bg:#333;
  --footer-bg:#1f1f1f;
  --footer-text:#c8c8c8;
  --line:#444;
}
*{box-sizing:border-box;margin:0;padding:0}
html,body{width:1200px;height:1146px;overflow:hidden;background:var(--black)}
body{position:relative;font-family:'Lato',sans-serif}
a{color:inherit;text-decoration:none}

.site-header{position:absolute;left:0;top:0;width:1200px;height:110px;background:var(--black)}
.brand{position:absolute;left:440px;top:20px;display:flex;align-items:center;gap:10px}
.brand-dot{width:72px;height:72px;border-radius:50%;background:#fff}
.brand-name{font-family:'Oswald',sans-serif;font-weight:600;font-size:38px;color:var(--brand-blue);line-height:1}
.follow{position:absolute;left:901px;top:55px;display:flex;align-items:center;gap:5px}
.follow-label{font-family:'Oswald',sans-serif;font-weight:600;font-size:12px;color:var(--orange);margin-right:4px}
.social-square{width:18px;height:18px;background:#4a6fb0;display:block}
.social-square.alt{background:#3aa6dc}

.main-nav{position:absolute;left:0;top:110px;width:1200px;height:47px;background:linear-gradient(var(--nav-top),var(--nav-bottom));border-top:1px solid #fff}
.search{position:absolute;left:130px;top:9px;width:338px;height:29px;background:#fff;border:1px solid #ccc;border-radius:2px;display:flex;align-items:center;padding-left:12px;gap:8px;font-family:'Pathway Gothic One',sans-serif;font-style:italic;font-size:16px;color:#999}
.menu{position:absolute;left:480px;top:0;height:46px;display:flex;list-style:none;border-left:1px solid #bbb}
.menu li{height:46px;border-right:1px solid #bbb;display:flex;align-items:center;justify-content:center;font-family:'Pathway Gothic One',sans-serif;font-size:20px;color:var(--nav-text)}

.hero{position:absolute;left:0;top:157px;width:1200px;height:305px}
.hero-photo{position:absolute;inset:0;background:radial-gradient(ellipse at 45% 45%,#6b7077 0%,#3d4045 40%,#17181a 80%),#222}
.hero-copy{position:absolute;left:660px;top:52px;width:310px;text-align:center;color:#fff}
.hero-kicker{font-family:'Oswald',sans-serif;font-weight:600;font-size:29px;color:var(--light-blue);line-height:38px}
.hero-title{font-family:'Oswald',sans-serif;font-weight:600;font-size:44px;line-height:47px;letter-spacing:1px}
.hero-sub{font-family:Arial,sans-serif;font-size:14px;margin-top:0}
.btn{display:inline-block;font-family:'Oswald',sans-serif;font-weight:600;color:#fff;text-transform:uppercase;border-radius:2px}
.btn-blue{background:linear-gradient(#1b7fd8,#0a48a8)}
.btn-dark{background:linear-gradient(#444,#111)}
.hero .btn{margin-top:11px;width:121px;height:41px;line-height:41px;font-size:19px}
.hero-arrow{position:absolute;top:137px}

.features{position:absolute;left:0;top:462px;width:1200px;height:420px;background:linear-gradient(#2b2b2b,var(--content-bg) 30%,#2e2e2e)}
.card{position:absolute;top:50px;width:290px;height:317px;background:var(--card-grey);text-align:center;color:#333}
.card.highlight{background:var(--deep-blue);color:#fff}
.card-photo{position:absolute;left:18px;top:13px;width:254px;height:119px;border:5px solid #fff;box-shadow:0 4px 6px rgba(0,0,0,.35)}
.card-title{position:absolute;left:0;top:152px;width:100%;font-family:'Oswald',sans-serif;font-weight:600;font-size:20px;color:var(--title-grey)}
.highlight .card-title{color:#fff}
.card-text{position:absolute;left:20px;top:186px;width:255px;text-align:left;font-size:11.5px;line-height:16px}
.card .btn{position:absolute;left:91px;top:254px;width:107px;height:38px;line-height:38px;font-size:17px}

.site-footer{position:absolute;left:0;top:882px;width:1200px;height:264px;background:var(--footer-bg)}
.footer-col{position:absolute;top:30px}
.footer-col h2{font-family:'Pathway Gothic One',sans-serif;font-weight:400;font-size:28px;color:var(--brand-blue);padding-left:22px;height:41px;border-bottom:1px solid var(--line)}
.footer-col ul{list-style:none}
.footer-col li{height:31px;line-height:31px;border-bottom:1px solid var(--line);padding-left:20px;font-size:13px;color:var(--footer-text);position:relative}
.footer-col li::before{content:"";position:absolute;left:4px;top:14px;border-left:5px solid #666;border-top:3px solid transparent;border-bottom:3px solid transparent}
.date{color:var(--orange)}
.footer-col li.copyright{color:var(--brand-blue)}
</style>
</head>
<body>
<header class="site-header">
  <div class="brand"><span class="brand-dot"></span><span class="brand-name">Brightway Merc</span></div>
  <div class="follow"><span class="follow-label">Follow Brightway Merc</span><a class="social-square" href="#" aria-label="Social page"></a><a class="social-square alt" href="#" aria-label="News feed"></a></div>
</header>

<nav class="main-nav">
  <div class="search">
    <svg width="18" height="18" viewBox="0 0 18 18"><circle cx="7" cy="7" r="5.5" fill="none" stroke="#555" stroke-width="1.6"/><line x1="11" y1="11" x2="16" y2="16" stroke="#555" stroke-width="1.8"/></svg>
    What are you looking for?
  </div>
  <ul class="menu">
    <li style="width:140px">Our products</li>
    <li style="width:137px">Our catalogues</li>
    <li style="width:105px">About us</li>
    <li style="width:116px">Contact us</li>
    <li style="width:82px">News</li>
  </ul>
</nav>

<section class="hero">
  <div class="hero-photo" role="img" aria-label="Campaign photo of two athletes in sports jackets against a stormy splash of water"></div>
  <svg class="hero-arrow" style="left:46px" width="20" height="32" viewBox="0 0 20 32"><polyline points="16,3 4,16 16,29" fill="none" stroke="#777" stroke-width="3"/></svg>
  <svg class="hero-arrow" style="left:1133px" width="20" height="32" viewBox="0 0 20 32"><polyline points="4,3 16,16 4,29" fill="none" stroke="var(--brand-blue)" stroke-width="3"/></svg>
  <div class="hero-copy">
    <p class="hero-kicker">LOREM IPSUM DOLOR</p>
    <h1 class="hero-title">SELEDENT<br>AMOR ET LESD</h1>
    <p class="hero-sub">Lorem ipsum dolor et se le delerent</p>
    <a class="btn btn-blue" href="#">Learn more</a>
  </div>
</section>

<main class="features">
  <article class="card highlight" style="left:142px">
    <div class="card-photo" role="img" aria-label="Photo of two runners in blue jackets on a night street" style="background:linear-gradient(135deg,#2b3550,#7a6a55 50%,#243046)"></div>
    <h2 class="card-title">PRODUCT OF THE MONTH</h2>
    <p class="card-text">Lorem ipsum dolor et me mensaje del a la nula estaba en la dolor. No em mehidian delibah meiserelifereba en tu model.</p>
    <a class="btn btn-blue" href="#">Read more</a>
  </article>
  <article class="card" style="left:454px">
    <div class="card-photo" role="img" aria-label="Photo of a woman training with dumbbells in a gym" style="background:linear-gradient(135deg,#d8d8d8,#8a8a8a 50%,#3a3a3a)"></div>
    <h2 class="card-title">NEWS</h2>
    <p class="card-text">Lorem ipsum dolor et me mensaje del a la nula estaba en la dolor. No em mehidian delibah meiserelifereba en tu model.</p>
    <a class="btn btn-dark" href="#">Read more</a>
  </article>
  <article class="card" style="left:768px">
    <div class="card-photo" role="img" aria-label="Photo of two athletes doing a drill in a sports hall" style="background:linear-gradient(135deg,#cfc7bd,#9a8a78 55%,#7a5a40)"></div>
    <h2 class="card-title">OTHER</h2>
    <p class="card-text">Lorem ipsum dolor et me mensaje del a la nula estaba en la dolor. No em mehidian delibah meiserelifereba en tu model.</p>
    <a class="btn btn-dark" href="#">Read more</a>
  </article>
</main>

<footer class="site-footer">
  <section class="footer-col" style="left:142px;width:188px">
    <h2>LINKS</h2>
    <ul><li>Our products</li><li>Our catalogues</li><li>About us</li><li>Contact us</li><li>News</li></ul>
  </section>
  <section class="footer-col" style="left:383px;width:398px">
    <h2>LATEST NEWS</h2>
    <ul>
      <li>Lorem ipsun dolor et mest et lerbare&nbsp; et&nbsp; <span class="date">(20/04/2013)</span></li>
      <li>Lorem ipsun dolor et mest et lerbare&nbsp; et el lap ter&nbsp; <span class="date">(20/04/2013)</span></li>
      <li>Lorem ipsun dolor et mest&nbsp; <span class="date">(20/04/2013)</span></li>
      <li>Lorem ipsun dolor et mest et lerbare&nbsp; et&nbsp; <span class="date">(20/04/2013)</span></li>
      <li>Lorem ipsun dolor et mest et lerbare lebrareista&nbsp; et&nbsp; <span class="date">(20/04/2013)</span></li>
    </ul>
  </section>
  <section class="footer-col" style="left:824px;width:233px">
    <h2>CONTACT US</h2>
    <ul>
      <li>Solberg vei 22 Oslo / Norway</li>
      <li>Telf: 23 45 78 90</li>
      <li>Fax:&nbsp; 23 45 78 90</li>
      <li>post@brightwaymerc.no</li>
      <li class="copyright">copyright © 2013 | Brightway Merc</li>
    </ul>
  </section>
</footer>
</body>
</html>
```